Swimming Pool Supply Company Business Cards

We need business cards designed for company. These need to be easy to edit so that we can fill in names, titles, and contact info for each person who works here.

Dalton R. Whitfield
Manager of Legal & Finance
K.L. Brisbane, Incorporated

4837 Grenway Avenue
Marlow Heights, PA 19243

E. dalton@klbrisbane-example.com
M. (215) 555-0173
O. (215) 555-0148

Contact Information for Business Card

Looking to upgrade current business cards with graphic that can be edited. Looking for fresh ideas for an age old industry.

Font styles to use
Serif
Sans Serif

Colors

Designer to choose colors to be used in the design.

Requirements
Must have
• Professional, fresh, unique but professional

```html
<!DOCTYPE html>
<html lang="en">
<head>
<meta charset="utf-8">
<title>Pool Supply Business Cards</title>
<link rel="stylesheet" href="https://fonts.googleapis.com/css2?family=Open+Sans:wght@400;600;700&display=swap">
<style>
  :root {
    --backdrop: #161616;
    --card: #262626;
    --card-edge: #303030;
    --ink: #ffffff;
    --ink-soft: #e4e4e4;
    --rule: #9a9a9a;
  }
  * { box-sizing: border-box; margin: 0; padding: 0; }
  html, body {
    width: 1200px; height: 912px; overflow: hidden;
    background: var(--backdrop);
    font-family: "Open Sans", Arial, sans-serif;
    color: var(--ink);
  }
  .canvas {
    width: 1200px; height: 912px;
    display: flex; flex-direction: column; align-items: center; justify-content: center;
    gap: 30px;
  }
  .card {
    width: 700px; height: 400px;
    background: var(--card);
    border: 1px solid var(--card-edge);
    border-radius: 3px;
    position: relative;
    box-shadow: 0 12px 30px rgba(0,0,0,.55);
  }
  /* front */
  .card-front { display: flex; align-items: center; justify-content: center; }
  .front-brand { text-align: left; }
  .front-brand .brand-name {
    font-size: 96px; font-weight: 700; letter-spacing: -1px; line-height: 1;
  }
  .front-brand .tagline {
    font-size: 22px; font-weight: 400; margin-top: 6px; letter-spacing: .2px;
  }
  /* back */
  .card-back { padding: 0; }
  .back-brand {
    position: absolute; left: 60px; top: 118px; width: 270px;
  }
  .back-brand .brand-name {
    font-size: 54px; font-weight: 700; letter-spacing: -1px; line-height: 1;
  }
  .back-brand .tagline { font-size: 12.5px; margin-top: 6px; }
  .divider {
    position: absolute; left: 360px; top: 70px; width: 1px; height: 150px;
    background: var(--rule);
  }
  .contact { position: absolute; left: 392px; top: 66px; }
  .contact .person-name { font-size: 21px; font-weight: 700; }
  .contact .person-title { font-size: 14px; color: var(--ink-soft); margin: 2px 0 14px; }
  .contact-list { list-style: none; }
  .contact-list li {
    display: flex; align-items: center; gap: 12px;
    font-size: 14px; line-height: 24px; color: var(--ink-soft);
  }
  .contact-list svg { width: 13px; height: 13px; fill: var(--ink); flex: none; }
  .address {
    position: absolute; left: 0; right: 0; bottom: 52px;
    text-align: center; font-size: 17px; letter-spacing: .2px;
  }
</style>
</head>
<body>
<main class="canvas">
  <section class="card card-front">
    <div class="front-brand">
      <div class="brand-name">BRISBANE</div>
      <div class="tagline">Big Enough to Serve You, Small Enough to Care</div>
    </div>
  </section>

  <section class="card card-back">
    <div class="back-brand">
      <div class="brand-name">BRISBANE</div>
      <div class="tagline">Swimming Pools, Supplies, and Accessories.</div>
    </div>
    <div class="divider"></div>
    <div class="contact">
      <div class="person-name">Dalton R. Whitfield</div>
      <div class="person-title">Manager of Legal &amp; Finance</div>
      <ul class="contact-list">
        <li>
          <svg viewBox="0 0 16 16" aria-hidden="true"><path d="M3.5 1l2.5 3-1.5 1.6c.9 2 2.4 3.5 4.4 4.4L10.5 8.5l3 2.5-1.4 2.9C7 13.6 2.4 9 2.1 3.9z"/></svg>
          (215) 555-0148
        </li>
        <li>
          <svg viewBox="0 0 16 16" aria-hidden="true"><path d="M4 0h8v16H4zM5.5 2v10h5V2zM7 13.2h2v1.4H7z" fill-rule="evenodd"/></svg>
          (215) 555-0173
        </li>
        <li>
          <svg viewBox="0 0 16 16" aria-hidden="true"><path d="M0 3h16v10H0zM1.5 4.2L8 9l6.5-4.8z" fill-rule="evenodd"/></svg>
          dalton@klbrisbane-example.com
        </li>
        <li>
          <svg viewBox="0 0 16 16" aria-hidden="true"><circle cx="8" cy="8" r="7.5"/><path d="M.5 8h15M8 .5v15M2 4h12M2 12h12" stroke="#262626" stroke-width="1" fill="none"/></svg>
          www.klbrisbane-example.com
        </li>
      </ul>
    </div>
    <div class="address">K.L. Brisbane, Incorporated &bull; 4837 Grenway Avenue &bull; Marlow Heights, PA 19243</div>
  </section>
</main>
</body>
</html>
```